Brackley Estate Agents - More in every move. Flyer

I need a double sided flyer designed that i will distribute to all the houses in town to try and drum up some business. The message i want to put across is that we offer a more inclusive service than any other agents in the town. We offer a number of services that other agents charge extra for but are included in our standard marketing.

These are things like Floorplans, Proffessionally enhanced Photos, Video Tours, and EPC's. We also have a USP that all of our Vendors get access to the 'SLC' (Seller Live Console) where they can get real time updates on the marketing of their We can tailor a service from scratch that suits the client making sure that they get exactly what they want. I will attach some versions of my logo etc.

The final design should communicate experience, professionalism and ability to give a great service. Ideally the final design will be modern and trendy but also timeless! It must also include our office contact details which are

Brackley Estate Agents, 14 Orchard Row, Stevenage, SG2 7PL.
Our telephone number is 01438 729184 Our lines are open 8am-8pm and our email address is info@brackleyhomesales.co.uk

I look forward to seeing some really cool designs! I know i'm asking for a lot but good luck!

Target Market(s)

Home owners that are thinking of selling.

Industry/Entity Type

Real Estate Agent

Font styles to use
Serif

Colors
f37122
1b1b1b

Requirements
Must have
• Our contact details, details of what we offer, a property theme. A colour reference to our logos.
Nice to have
• Stunning design.
Should not have
• The smell of desperation! Anything saying 'Real Estate'. Its an English company so we are just Estate Agents. Apologies if you know that already, i dont know who this will go to.

```html
<!DOCTYPE html>
<html lang="en">
<head>
<meta charset="utf-8">
<title>Brackley Estate Agents – Flyer</title>
<link href="https://fonts.googleapis.com/css2?family=Playfair+Display:wght@400;700&family=Roboto:wght@300;400;700&family=Oswald:wght@600&display=swap" rel="stylesheet">
<style>
  :root{
    --orange:#f37122;
    --orange-deep:#d9431f;
    --ink:#1b1b1b;
    --panel-top:#3b3b3b;
    --panel-bottom:#262626;
    --panel-edge:#575757;
    --stage:#86a3a3;
    --white:#ffffff;
    --muted:#d6d6d6;
  }
  *{box-sizing:border-box;margin:0;padding:0}
  html,body{width:1200px;height:960px;overflow:hidden}
  body{background:var(--stage);font-family:'Roboto',sans-serif;position:relative}
  h1,h2,h3{font-weight:400}
  .side-label{position:absolute;top:62px;width:520px;text-align:center;color:var(--white);font-family:'Roboto',sans-serif;font-weight:300;font-size:46px;letter-spacing:1px}
  .side-label--front{left:52px}
  .side-label--back{left:622px}

  .flyer{position:absolute;top:150px;width:520px;height:736px;background:var(--ink);overflow:hidden}
  .flyer--front{left:52px}
  .flyer--back{left:622px}
  .flyer__bg{position:absolute;inset:0;width:520px;height:736px}

  .brand{position:absolute;display:flex;align-items:center;gap:8px}
  .brand__dot{width:46px;height:46px;border-radius:50%;background:var(--orange);border:3px solid var(--ink);box-shadow:0 0 0 2px var(--orange)}
  .brand__name{font-family:'Playfair Display',serif;color:var(--orange);font-size:40px;line-height:1}
  .brand__tag{display:block;font-family:'Playfair Display',serif;color:var(--orange);font-size:8px;text-align:right;margin-top:2px}

  .lede{position:absolute;left:13px;top:92px}
  .lede__title{font-family:'Playfair Display',serif;color:var(--orange-deep);font-size:25px;line-height:1.1;font-weight:400}
  .lede__text{font-family:'Playfair Display',serif;color:var(--ink);font-size:13px;line-height:17px;margin-top:4px}

  .welcome{position:absolute;left:21px;right:19px;top:358px;font-family:'Playfair Display',serif;font-size:31px;line-height:38px;font-weight:400}
  .welcome__line1{display:block;color:var(--white)}
  .welcome__line2{color:var(--orange);display:flex;align-items:center;gap:6px;white-space:nowrap;font-size:30px}
  .welcome__line2::after{content:"";flex:1;height:1px;background:var(--muted)}

  .intro{position:absolute;left:19px;right:19px;top:443px;color:var(--white);font-weight:300;font-size:9.3px;line-height:14.2px}

  .cards{position:absolute;left:19px;right:19px;display:flex;justify-content:space-between}
  .cards--front{top:541px}
  .cards--back{top:419px}
  .card{position:relative;width:145px;height:122px;background:linear-gradient(var(--panel-top),var(--panel-bottom));border:1px solid var(--panel-edge);text-align:center;color:var(--white);padding-top:40px;box-shadow:0 2px 6px rgba(0,0,0,.5)}
  .cards--back .card{height:139px;padding-top:44px}
  .card__icon{position:absolute;left:50%;top:-30px;margin-left:-30px;width:60px;height:60px;border-radius:50%;background:var(--orange-deep);border:2px solid var(--white);box-shadow:0 0 0 2px var(--ink);display:flex;align-items:center;justify-content:center}
  .card__title{font-family:'Playfair Display',serif;font-size:17px;color:var(--orange-deep);font-weight:400;white-space:nowrap}
  .cards--back .card__title{color:var(--white);font-size:17px;letter-spacing:.5px}
  .card__text{font-weight:300;font-size:7.4px;line-height:11px;padding:4px 8px 0;text-align:justify;text-align-last:center}
  .card__list{list-style:none;font-weight:300;font-size:9.3px;line-height:17.5px;margin-top:6px}

  .services-title{position:absolute;left:18px;top:138px;font-family:'Playfair Display',serif;font-size:27px;line-height:34px;font-weight:400;color:var(--white);width:212px;white-space:nowrap;border-bottom:1px solid #777;padding-bottom:6px}
  .services-title span{color:var(--orange-deep)}
  .services-text{position:absolute;left:19px;top:197px;width:222px;color:var(--white);font-weight:300;font-size:9.3px;line-height:14px;text-align:justify}
  .promise{position:absolute;left:18px;top:324px;font-family:'Playfair Display',serif;white-space:nowrap}
  .promise__head{color:var(--orange-deep);font-size:14.2px}
  .promise__sub{color:var(--white);font-size:13.4px;margin-top:2px}

  .hours{position:absolute;left:0;right:0;top:583px;text-align:center;font-family:'Oswald',sans-serif;font-weight:600;font-size:34px;color:var(--white);letter-spacing:.5px}
  .hours span{color:var(--orange)}
  .listings{position:absolute;left:34px;right:40px;top:638px;display:flex;justify-content:space-between;align-items:center}
  .listing-badge{height:22px;border-radius:3px}

  .footer__web{position:absolute;left:0;right:0;top:682px;height:18px;background:linear-gradient(#b5b5b5,#8f8f8f)}
  .footer__web-tab{position:absolute;left:112px;right:112px;top:-2px;height:20px;background:linear-gradient(#e2e2e2,#bdbdbd);clip-path:polygon(4% 0,96% 0,100% 100%,0 100%);text-align:center;font-weight:700;font-size:12.4px;line-height:20px;color:var(--ink);letter-spacing:.3px}
  .footer__contact{position:absolute;left:0;right:0;top:700px;height:36px;background:linear-gradient(var(--orange),var(--orange-deep));display:flex;align-items:center;justify-content:center;gap:12px;color:var(--white);font-size:7.8px;font-weight:300;white-space:nowrap}
  .footer__item{display:flex;align-items:center;gap:4px}
</style>
</head>
<body>

<div class="side-label side-label--front">Front</div>
<div class="side-label side-label--back">Back</div>

<!-- FRONT SIDE -->
<section class="flyer flyer--front">
  <svg class="flyer__bg" viewBox="0 0 520 736">
    <defs>
      <linearGradient id="scene" x1="0" y1="0" x2="0" y2="1">
        <stop offset="0" stop-color="#dcecf7"/>
        <stop offset=".38" stop-color="#a8cde6"/>
        <stop offset=".55" stop-color="#6f8f5a"/>
        <stop offset=".72" stop-color="#a8675a"/>
        <stop offset=".85" stop-color="#7e7f80"/>
        <stop offset="1" stop-color="#6aa43b"/>
      </linearGradient>
      <linearGradient id="swoosh" x1="0" y1="0" x2="1" y2="0">
        <stop offset="0" stop-color="#f37122"/>
        <stop offset="1" stop-color="#c9301c"/>
      </linearGradient>
    </defs>
    <rect width="520" height="736" fill="#1b1b1b"/>
    <circle cx="200" cy="520" r="190" fill="none" stroke="#222" stroke-width="26"/>
    <path d="M0,38 C160,18 330,60 520,108 L520,125 C330,80 160,42 0,52 Z" fill="url(#swoosh)"/>
    <path role="img" aria-label="Photograph of Stevenage streets, apartment blocks and a green roundabout under a blue sky" d="M0,50 C160,40 330,80 520,122 L520,362 C380,352 250,300 0,265 Z" fill="url(#scene)"/>
    <path d="M0,258 C230,290 370,350 520,356 L520,362 C380,356 250,330 0,288 Z" fill="#5a5a5a"/>
    <path d="M0,266 C200,300 330,345 520,362 L520,370 C330,362 200,330 0,290 Z" fill="url(#swoosh)"/>
  </svg>

  <div class="brand" style="left:296px;top:18px">
    <div class="brand__dot"></div>
    <div>
      <span class="brand__name">Brackley</span>
      <span class="brand__tag">Estate Agents</span>
    </div>
  </div>

  <div class="lede">
    <h2 class="lede__title">Brackley Estate Agents</h2>
    <p class="lede__text">aim is to give each client everything they<br>need to help them along their property 'journey'.</p>
  </div>

  <h1 class="welcome">
    <span class="welcome__line1">WELCOME TO</span>
    <span class="welcome__line2">BRACKLEY ESTATE AGENTS</span>
  </h1>

  <p class="intro">Brackley Estate Agents specialise in residential sales, lettings and property management. Our experienced team can advise you on just about everything from decor to financial advice, we have it covered! With a wealth of combined experienced and local knowledge covering Stevenage and the surrounding areas, you can be comfortable leaving the task in our hands!</p>

  <div class="cards cards--front">
    <article class="card">
      <div class="card__icon">
        <svg width="32" height="32" viewBox="0 0 32 32"><path d="M16 4 L3 16 H7 V28 H13 V20 H19 V28 H25 V16 H29 Z" fill="#1b1b1b"/></svg>
      </div>
      <h3 class="card__title">Book a Valuation</h3>
      <p class="card__text">Take advantage of a free no obligation valuation and our competitive selling fee and experience the difference for yourself!</p>
    </article>
    <article class="card">
      <div class="card__icon">
        <svg width="32" height="32" viewBox="0 0 32 32"><path d="M22 4 L28 10 L12 26 L5 27 L6 20 Z" fill="#1b1b1b"/><path d="M19 7 L25 13" stroke="#d9431f" stroke-width="2"/></svg>
      </div>
      <h3 class="card__title">Register With Us</h3>
      <p class="card__text">Want to stay up to date with properties you might be interested in? Register with us to receive regular property updates</p>
    </article>
    <article class="card">
      <div class="card__icon">
        <svg width="32" height="32" viewBox="0 0 32 32"><circle cx="16" cy="11" r="6.5" fill="#1b1b1b"/><path d="M4 29 C5 21 10 19 16 19 C22 19 27 21 28 29 Z" fill="#1b1b1b"/></svg>
      </div>
      <h3 class="card__title">Ask an Expert</h3>
      <p class="card__text">Do you have a property related question? Click here to ask your local expert!</p>
    </article>
  </div>

  <footer>
    <div class="footer__web"><div class="footer__web-tab">WWW.BRACKLEYHOMESALES.CO.UK</div></div>
    <div class="footer__contact">
      <span class="footer__item"><svg width="8" height="10" viewBox="0 0 8 10"><path d="M4 0 C1.8 0 0 1.7 0 3.8 C0 6.5 4 10 4 10 C4 10 8 6.5 8 3.8 C8 1.7 6.2 0 4 0 Z" fill="#fff"/><circle cx="4" cy="3.8" r="1.4" fill="#e05020"/></svg>Brackley Estate Agents, 14 Orchard Row, Stevenage, SG2 7PL.</span>
      <span class="footer__item"><svg width="9" height="9" viewBox="0 0 10 10"><path d="M2 0 L4 2.5 L3 4 C4 6 5 7 6 7 L7.5 6 L10 8 L8.5 10 C4 10 0 6 0 1.5 Z" fill="#fff"/></svg>01438 729184</span>
      <span class="footer__item"><svg width="10" height="7" viewBox="0 0 10 7"><rect width="10" height="7" fill="#fff"/><path d="M0 0 L5 4 L10 0" stroke="#e05020" fill="none"/></svg>info@brackleyhomesales.co.uk</span>
    </div>
  </footer>
</section>

<!-- BACK SIDE -->
<section class="flyer flyer--back">
  <svg class="flyer__bg" viewBox="0 0 520 736">
    <defs>
      <linearGradient id="swooshB" x1="0" y1="0" x2="1" y2="0">
        <stop offset="0" stop-color="#f37122"/>
        <stop offset="1" stop-color="#c9301c"/>
      </linearGradient>
      <linearGradient id="portrait" x1="0" y1="0" x2="1" y2="1">
        <stop offset="0" stop-color="#e2e2e2"/>
        <stop offset="1" stop-color="#7a7a7a"/>
      </linearGradient>
      <clipPath id="teamClip"><circle cx="399" cy="164" r="126"/></clipPath>
    </defs>
    <rect width="520" height="736" fill="#1b1b1b"/>
    <path d="M0,98 C170,112 330,80 520,22 L520,34 C330,92 170,122 0,108 Z" fill="#5a5a5a"/>
    <path d="M0,102 C170,112 330,78 520,24 L520,30 C330,86 170,118 0,110 Z" fill="url(#swooshB)"/>
    <g clip-path="url(#teamClip)">
      <rect role="img" aria-label="Portrait of a team member over a street map" x="273" y="38" width="126" height="126" fill="url(#portrait)"/>
      <rect role="img" aria-label="Portrait of a team member over a street map" x="399" y="38" width="126" height="126" fill="url(#portrait)"/>
      <rect role="img" aria-label="Portrait of a team member over a street map" x="273" y="164" width="126" height="126" fill="url(#portrait)"/>
      <rect role="img" aria-label="Portrait of a team member over a street map" x="399" y="164" width="126" height="126" fill="url(#portrait)"/>
      <rect x="396" y="38" width="6" height="252" fill="#fff"/>
      <rect x="273" y="161" width="252" height="6" fill="#fff"/>
    </g>
    <circle cx="399" cy="164" r="126" fill="none" stroke="#fff" stroke-width="2"/>
    <circle cx="399" cy="164" r="25" fill="#f37122" stroke="#1b1b1b" stroke-width="4"/>
  </svg>

  <div class="brand" style="left:18px;top:14px">
    <div class="brand__dot"></div>
    <div>
      <span class="brand__name">Brackley</span>
      <span class="brand__tag">Estate Agents</span>
    </div>
  </div>

  <h2 class="services-title">OUR <span>SERVICES</span></h2>
  <p class="services-text">At Brackley Estate Agents we pride ourselves on the level of service we provide. We know that this is going to be one of the biggest transactions you make during your lifetime and we believe that it should be treated as such. We achieve this by giving a truly unique service with a fully inclusive marketing package that remains unchallenged in the local market.</p>

  <div class="promise">
    <p class="promise__head">WE DOES PROVIDE A CUSTOMIZED PLAN TO SERVE YOU THE BEST!</p>
    <p class="promise__sub">We offer 'SLC' to our Valuable customers to get real time update on Marketing.</p>
  </div>

  <div class="cards cards--back">
    <article class="card">
      <div class="card__icon">
        <svg width="32" height="32" viewBox="0 0 32 32"><rect x="5" y="20" width="4" height="8" fill="#fff"/><rect x="11" y="16" width="4" height="12" fill="#fff"/><rect x="17" y="13" width="4" height="15" fill="#fff"/><rect x="23" y="9" width="4" height="19" fill="#fff"/><path d="M4 16 L12 9 L17 12 L26 4" stroke="#fff" stroke-width="2" fill="none"/><path d="M22 3 L28 3 L28 9" stroke="#fff" stroke-width="2" fill="none"/></svg>
      </div>
      <h3 class="card__title">SALES</h3>
      <ul class="card__list"><li>Better As Standard</li><li>Keeping You In The Loop!</li><li>When Its All Said and Done.</li></ul>
    </article>
    <article class="card">
      <div class="card__icon">
        <svg width="32" height="32" viewBox="0 0 32 32"><rect x="5" y="5" width="22" height="16" rx="2" fill="#fff"/><rect x="14" y="21" width="4" height="8" fill="#fff"/><path d="M11 13 L15 17 L22 9" stroke="#d9431f" stroke-width="2.5" fill="none"/></svg>
      </div>
      <h3 class="card__title">LETTINGS</h3>
      <ul class="card__list"><li>Let Only</li><li>Gold Management</li><li>Diamond Management</li></ul>
    </article>
    <article class="card">
      <div class="card__icon">
        <svg width="32" height="32" viewBox="0 0 32 32"><path d="M16 4 L3 16 H7 V28 H25 V16 H29 Z" fill="#fff"/><path d="M16 14 V24 M11 19 H21" stroke="#d9431f" stroke-width="2.5"/></svg>
      </div>
      <h3 class="card__title">ADDITIONAL</h3>
      <ul class="card__list"><li>Financial Services</li><li>Solicitors</li><li>Extras</li></ul>
    </article>
  </div>

  <p class="hours">OUR LINES ARE OPEN <span>8AM-8PM</span></p>

  <div class="listings">
    <div class="listing-badge" style="width:128px;background:#2fa39a"></div>
    <div class="listing-badge" style="width:128px;background:#6a2b8a"></div>
    <div class="listing-badge" style="width:148px;background:#1f7fc4"></div>
  </div>

  <footer>
    <div class="footer__web"><div class="footer__web-tab">WWW.BRACKLEYHOMESALES.CO.UK</div></div>
    <div class="footer__contact">
      <span class="footer__item"><svg width="8" height="10" viewBox="0 0 8 10"><path d="M4 0 C1.8 0 0 1.7 0 3.8 C0 6.5 4 10 4 10 C4 10 8 6.5 8 3.8 C8 1.7 6.2 0 4 0 Z" fill="#fff"/><circle cx="4" cy="3.8" r="1.4" fill="#e05020"/></svg>Brackley Estate Agents, 14 Orchard Row, Stevenage, SG2 7PL.</span>
      <span class="footer__item"><svg width="9" height="9" viewBox="0 0 10 10"><path d="M2 0 L4 2.5 L3 4 C4 6 5 7 6 7 L7.5 6 L10 8 L8.5 10 C4 10 0 6 0 1.5 Z" fill="#fff"/></svg>01438 729184</span>
      <span class="footer__item"><svg width="10" height="7" viewBox="0 0 10 7"><rect width="10" height="7" fill="#fff"/><path d="M0 0 L5 4 L10 0" stroke="#e05020" fill="none"/></svg>info@brackleyhomesales.co.uk</span>
    </div>
  </footer>
</section>

</body>
</html>
```